Professional IT Company Letterhead

We need a new letterhead design to incorporate our new login and business card design recently received here on Pixel Meadow. We want the same look and feel as the other two accepted projects. We want a professional and clean design.

Target Market(s)

Medical/Dental and Professional Services Businesses (CPA, Attorney, Architect etc)

Industry/Entity Type

Business

Requirements
Must have
• Clean and professional, consistent brand with our current design of our new logo and business cards.
Nice to have
• Would like to also be able to use the design on our newsletter header

```html
<!DOCTYPE html>
<html lang="en">
<head>
<meta charset="utf-8">
<title>Tidewell Systems Letterhead</title>
<link href="https://fonts.googleapis.com/css2?family=Open+Sans:wght@300;400;600;700&family=Dancing+Script:wght@500&family=Quicksand:wght@400&display=swap" rel="stylesheet">
<style>
  :root {
    --ink: #2b2b2b;
    --muted: #555555;
    --brand-blue: #1e9fe0;
    --brand-deep: #0d6fb8;
    --line-blue: #2a7fc4;
    --ghost: #e6e7e9;
    --paper: #ffffff;
  }
  * { margin: 0; padding: 0; box-sizing: border-box; }
  html, body { width: 927px; height: 1200px; overflow: hidden; background: var(--paper); }
  .letterhead {
    position: relative;
    width: 927px;
    height: 1200px;
    overflow: hidden;
    font-family: "Open Sans", Arial, sans-serif;
    color: var(--ink);
  }
  .mascot-backdrop {
    position: absolute;
    left: 285px; top: 620px;
    width: 640px; height: 580px;
    background: radial-gradient(ellipse at 45% 45%, rgba(230,231,233,0.75) 0%, rgba(230,231,233,0.35) 55%, rgba(255,255,255,0) 75%);
  }
  .brand {
    position: absolute;
    left: 108px; top: 100px;
    display: flex; align-items: center; gap: 10px;
  }
  .brand-mark { width: 18px; height: 18px; background: var(--brand-blue); }
  .brand-name {
    font-size: 34px; font-weight: 600; color: var(--brand-blue);
    letter-spacing: -0.5px;
  }
  .date {
    position: absolute; right: 105px; top: 238px;
    font-size: 14.5px;
  }
  .recipient {
    position: absolute; left: 109px; top: 278px;
    font-size: 14.5px; line-height: 18.5px;
  }
  .recipient-name { font-weight: 700; font-size: 15px; margin-bottom: 3px; }
  .body-copy {
    position: absolute; left: 109px; top: 406px; width: 708px;
    font-size: 14.6px; line-height: 18.2px; text-align: justify;
  }
  .body-copy p { margin-bottom: 18.2px; }
  .body-copy p.lead { text-indent: 55px; }
  .signoff {
    position: absolute; left: 109px; top: 768px;
  }
  .signoff-greeting { font-size: 17.5px; color: var(--muted); }
  .signature {
    font-family: "Dancing Script", cursive;
    font-size: 52px; line-height: 64px; color: #1f1f1f; margin-top: -2px;
  }
  .signer-name { font-size: 18px; line-height: 22px; margin-top: -4px; }
  .signer-title { font-size: 15px; font-weight: 300; color: var(--muted); }
  .contact-bar {
    position: absolute; left: 204px; top: 1022px;
    display: flex; font-family: "Quicksand", sans-serif;
    font-size: 10.6px; line-height: 14px; color: var(--brand-blue);
  }
  .contact-item {
    text-align: center; padding: 0 6px;
  }
  .contact-item + .contact-item { border-left: 1.5px solid var(--line-blue); }
  .contact-item.address { width: 190px; }
  .contact-item.phone { width: 148px; }
  .contact-item.web { width: 180px; }
  .contact-icon {
    display: block; width: 23px; height: 19px; margin: 2px auto 12px;
    background: var(--brand-blue);
    border-radius: 0 0 10px 0;
  }
  .water-band {
    position: absolute; left: 0; top: 1118px; width: 927px; height: 66px;
    background: linear-gradient(180deg, rgba(255,255,255,0) 0%, rgba(120,190,235,0.55) 30%, #1a76c2 50%, rgba(120,190,235,0.5) 68%, rgba(255,255,255,0) 100%);
  }
</style>
</head>
<body>
<div class="letterhead">
  <div class="mascot-backdrop" role="img" aria-label="Faint large brand mascot decoration"></div>

  <div class="brand">
    <span class="brand-mark"></span>
    <span class="brand-name">Tidewell Systems</span>
  </div>

  <div class="date">Date, 17 December 2015</div>

  <div class="recipient">
    <div class="recipient-name">MARA ELLISON KENT</div>
    <div>7-9, New Shire Street,</div>
    <div>NA, Nation 20555</div>
  </div>

  <div class="body-copy">
    <p class="lead">Lorem ipsum dolor sit amet, consectetur adipiscing elit, sed do eiusmod tempor incididunt ut labore et dolore magna aliqua. Ut enim ad minim veniam, quis nostrud exercitation ullamco laboris nisi ut aliquip ex ea commodo consequat. Duis aute irure dolor in reprehenderit in voluptate velit esse cillum dolore eu fugiat nulla pariatur. Excepteur sint occaecat cupidatat non proident, sunt in culpa qui officia deserunt mollit anim id est laborum.</p>
    <p>Lorem ipsum dolor sit amet, consectetur adipiscing elit, sed do eiusmod tempor incididunt ut labore et dolore magna aliqua. Ut enim ad minim veniam, quis nostrud exercitation ullamco laboris nisi ut aliquip ex ea commodo consequat. Duis aute irure dolor in reprehenderit in voluptate velit esse cillum dolore eu fugiat nulla pariatur. Excepteur sint occaecat cupidatat non proident, sunt in culpa qui officia deserunt mollit anim id est laborum.</p>
    <p>Lorem ipsum dolor sit amet, consectetur adipiscing elit, sed do eiusmod tempor incididunt ut labore et dolore magna aliqua. Ut enim ad minim veniam, quis nostrud exercitation ullamco laboris nisi ut aliquip ex ea commodo consequat. Duis aute irure dolor in reprehenderit in voluptate velit esse cillum dolore eu fugiat nulla pariatur. Excepteur sint occaecat cupidatat non proident, sunt in culpa qui officia deserunt mollit anim id est laborum.</p>
  </div>

  <div class="signoff">
    <div class="signoff-greeting">regard</div>
    <div class="signature">Owen Parker</div>
    <div class="signer-name">Owen Hale Parker</div>
    <div class="signer-title">General Manger</div>
  </div>

  <div class="contact-bar">
    <div class="contact-item address">
      <span class="contact-icon"></span>
      1820 Willow Bend Road, Ste. B<br>Brookfield, Ohio 44403
    </div>
    <div class="contact-item phone">
      <span class="contact-icon"></span>
      +555 204 3318<br>+555 204 7762
    </div>
    <div class="contact-item web">
      <span class="contact-icon"></span>
      office@tidewellsystems.com<br>www.tidewellsystems.com
    </div>
  </div>

  <div class="water-band" role="img" aria-label="Splashing water surface band"></div>
</div>
</body>
</html>
```